VELDA Metals - newly established Metal trading business

Velda Metals is a newly established Metal trading, processing and refining business

we are looking for a simple and professional business website, which is easy to navigate

We will be selling metal / commodities to some of the largest industrial business globally. Therefore the website must make us look like a large and reputable business.

We have attached a Powerpoint presentation with some ideas

Target Market(s)

Lagre metal consumers

Industry/Entity Type

Commodity

Logo Text

VELDA Metals Group

Coding

Coded - Design and coding required

Number of Pages Required

5+ page

Font styles to use
Sans Serif

Colors

Designer to choose colors to be used in the design.

Requirements
Must have
• - fixed menu bar at the top
• - continuous scroll down function
• - multiple tabs left and right for more information
• - have dynamic screen size adjustment / a mobile version
• - google maps

```html
<!DOCTYPE html>
<html lang="en">
<head>
<meta charset="utf-8">
<title>VELDA Metals Group</title>
<link href="https://fonts.googleapis.com/css2?family=Lato:wght@400;700;900&display=swap" rel="stylesheet">
<style>
:root{
  --orange:#c95316;
  --dark:#222222;
  --footer:#262626;
  --text:#555555;
  --heading:#2b2b2b;
  --white:#ffffff;
  --line:#d9a27f;
}
*{margin:0;padding:0;box-sizing:border-box}
html,body{width:1200px;height:3273px;overflow:hidden}
body{font-family:'Lato',sans-serif;color:var(--text);background:var(--white);position:relative}
.abs{position:absolute}
.site-header{top:0;left:0;width:1200px;height:83px;background:var(--dark)}
.brand{left:131px;top:16px;color:var(--white)}
.brand-mark{display:inline-block;width:34px;height:34px;border-radius:50%;background:#8a8a8a;vertical-align:middle;margin-right:8px}
.brand-name{font-size:26px;font-weight:900;vertical-align:middle;letter-spacing:.5px}
.brand-sub{display:block;font-size:11px;letter-spacing:.5px;margin-top:2px}
.main-nav{right:131px;top:33px;display:flex;gap:34px}
.main-nav a{color:var(--white);font-size:13px;font-weight:700;text-decoration:none;letter-spacing:.3px;padding-bottom:7px}
.main-nav a.active{border-bottom:3px solid var(--orange)}
.hero{top:83px;left:0;width:1200px;height:462px;background:linear-gradient(120deg,#6f6a60 0%,#8d8577 35%,#a08c5f 65%,#d7a44a 85%,#4a3b22 100%)}
.hero-title{left:131px;top:80px;color:var(--white);font-size:48px;font-weight:700;line-height:52px}
.steps{left:131px;top:208px;display:flex;gap:32px}
.step{width:56px;text-align:center;color:var(--white);font-size:12px;font-weight:700}
.step-num{width:54px;height:54px;border-radius:50%;border:3px solid var(--white);background:var(--orange);line-height:48px;font-size:15px;font-weight:400;margin-bottom:6px}
.step-num.first{background:var(--white);color:var(--heading)}
.step-label{white-space:nowrap;margin-left:-10px;width:76px}
.btn{left:131px;top:339px;width:149px;height:44px;background:var(--orange);color:var(--white);border-radius:22px;font-size:14px;font-weight:700;text-align:center;line-height:44px}
.chev{left:584px;top:422px}
.section-title{font-size:28px;font-weight:700;color:var(--heading)}
.section-title span{color:var(--orange)}
.about-title{left:131px;top:622px}
.about-col{top:675px;width:440px;font-size:12px;line-height:26px}
.commodities{top:925px;left:0;width:1200px;height:519px;background:linear-gradient(180deg,#bcd5e6 0%,#d9e7ef 55%,#7fa6c0 72%,#4f87ac 100%)}
.commod-title{left:0;width:1200px;top:980px;text-align:center}
.commod-list{top:1052px;width:260px;list-style:none;font-size:13px;font-weight:700;color:var(--heading);line-height:25px}
.commod-list li{padding-left:18px;position:relative}
.commod-list li::before{content:"»";position:absolute;left:0;color:var(--heading)}
.arrow-btn{top:1110px;width:36px;height:36px;border-radius:50%;background:rgba(255,255,255,.7);text-align:center;line-height:34px;color:#555;font-size:18px}
.services-title{left:131px;top:1521px}
.service{width:462px;border:1px solid var(--line);padding:22px 28px;font-size:10.5px;line-height:23px}
.service h3{font-size:19px;font-weight:400;color:var(--heading);text-align:center;margin-bottom:12px}
.map{top:2317px;left:0;width:1200px;height:417px;background:linear-gradient(135deg,#e4e4e4,#d6d6d6 50%,#e8e8e8)}
.office{top:2780px;width:288px;height:185px;border:1px solid #777;padding:20px 28px;font-size:12px;line-height:28px}
.office h4{font-size:17px;font-weight:400;text-decoration:underline;text-align:center;color:var(--heading);margin-bottom:6px}
.office .row{display:flex;gap:10px;align-items:flex-start}
.office svg{flex:none;margin-top:8px}
.office.hl{background:var(--orange);color:var(--white);border-color:var(--orange)}
.office.hl h4{color:var(--white)}
.site-footer{top:3050px;left:0;width:1200px;height:223px;background:var(--footer)}
.footer-brand{left:131px;top:3092px;color:var(--white)}
.footer-links{right:131px;top:3102px;color:var(--white);font-size:12px}
.social{right:131px;top:3140px;display:flex;gap:12px}
.social span{width:34px;height:34px;border-radius:50%;background:var(--orange);display:block}
.footer-rule{left:131px;top:3222px;width:938px;height:1px;background:#666}
.copyright{left:0;width:1200px;top:3238px;text-align:center;color:#ccc;font-size:11px}
</style>
</head>
<body>

<header class="abs site-header">
  <div class="abs brand"><span class="brand-mark"></span><span class="brand-name">VELDA</span><span class="brand-sub">METALS GROUP</span></div>
  <nav class="abs main-nav">
    <a class="active">HOME</a><a>ABOUT</a><a>COMMODITIES</a><a>SERVICES</a><a>CONTACT</a><a>LOG IN</a>
  </nav>
</header>

<section class="abs hero" role="img" aria-label="Photograph of an excavator at a quarry at sunset">
  <h1 class="abs hero-title">METALS AND ASSOCIATED<br>RAW MATERIALS</h1>
  <div class="abs steps">
    <div class="step"><div class="step-num first">1</div><div class="step-label">SOURCE</div></div>
    <div class="step"><div class="step-num">2</div><div class="step-label">TRANSPORT</div></div>
    <div class="step"><div class="step-num">3</div><div class="step-label">STORE</div></div>
    <div class="step"><div class="step-num">4</div><div class="step-label">DELIVER</div></div>
  </div>
  <div class="abs btn">READ MORE</div>
  <svg class="abs chev" width="32" height="20" viewBox="0 0 32 20"><path d="M3 4 L16 16 L29 4" fill="none" stroke="#fff" stroke-width="4"/></svg>
</section>

<h2 class="abs section-title about-title"><span>About</span> VELDA</h2>
<p class="abs about-col" style="left:131px">Velda Metals is a global commodities group with an established presence throughout the metal markets. Velda Metals has a strong focus on consolidating, processing, and trading a full range of physical metal commodities, having established both European processing facilities and trading offices. Our network of clients and partners range from international metal producers, sovereigns, independent operators and industrial consumers.</p>
<p class="abs about-col" style="left:648px">The VELDA team is entrepreneurial and builds solutions for relationships based on transparency and trust. VELDA strives to be a supplier, partner and market participant that delivers value-added services to producers and consumers of commodities by managing the market risk, operational risk and quality risk inherent in the global commodity markets.</p>

<section class="abs commodities" role="img" aria-label="Photograph of a container ship at sea under a pale sky"></section>
<h2 class="abs section-title commod-title"><span>Commodities -</span> MAGNESIUM</h2>
<div class="abs arrow-btn" style="left:200px">‹</div>
<div class="abs arrow-btn" style="left:968px">›</div>
<ul class="abs commod-list" style="left:337px">
  <li>99.7% – 99.85% primary aluminium</li><li>Master alloys</li><li>Copper manganese</li><li>Copper iron</li><li>Copper Phosphor 85/90 – waffle &amp; shot form</li>
</ul>
<ul class="abs commod-list" style="left:650px;width:290px">
  <li>High grade copper alloy scrap</li><li>Copper nickel</li><li>Copper Granules</li><li>Various grades and sizes available</li><li>Copper nickel, nickel brass &amp; silver, aluminium bronze.</li>
</ul>

<h2 class="abs section-title services-title"><span>Our</span> SERVICES</h2>
<div class="abs service" style="left:131px;top:1586px;height:301px">
  <h3>TRADING &amp; SOURCING</h3>
  <p>VELDA's experienced trading team has a wealth of knowledge throughout the global metal markets.</p>
  <p>VELDA sources refined metals of various grades from smelters and the associated raw materials from mines and refineries. Our partnerships and relationships with suppliers allow VELDA to provide a reliable and flexible service to customers with short and long term supply agreements and just in time spot transactions.</p>
  <p>The VELDA team is a reliable sourcing partner to secure the raw materials any industrial business needs on time, on specification and as needed. VELDA is able to access a global supplier base and optimise pricing for raw materials among its activities.</p>
</div>
<div class="abs service" style="left:607px;top:1586px;height:301px">
  <h3>PROCESSING &amp; CONSOLIDATING</h3>
  <p>VELDA operates a physical processing and consolidation plant in the UK, responsible for processing and refining a wide variety of metallic scraps and alloys.</p>
  <p>VELDA is a vertically integrated commodity group and vero eos et accusamus et iusto odio dignissimos ducimus qui blanditiis praesentium voluptatum deleniti atque corrupti quos dolores et quas molestias excepturi sint occaecati cupiditate non provident, similique sunt in culpa qui officia deserunt mollitia animi, id est laborum et dolorum fuga.</p>
  <p>Et harum quidem rerum facilis est et expedita distinctio. Nam libero tempore, cum soluta nobis est eligendi optio cumque nihil impedit quo minus id quod.</p>
</div>
<div class="abs service" style="left:131px;top:1905px;height:303px">
  <h3>OPERATIONAL SECURITY</h3>
  <p>VELDA's senior leadership has experience across the commodity value chain including: risk management, marketing arrangements, commodity asset management, leadership of commodity production assets, lending to commodity producers and consumers and logistics management.</p>
  <p>VELDA aims to add value to all its partners, suppliers and customers by providing services that enhance their business profitability, optimise commodity production or manage balance sheets.</p>
</div>
<div class="abs service" style="left:607px;top:1905px;height:303px">
  <h3>OUTSOURCED SOLUTIONS</h3>
  <p>Et harum quidem rerum facilis est et expedita distinctio. Nam libero tempore, cum soluta nobis est eligendi optio cumque nihil impedit quo minus id quod maxime placeat facere possimus, omnis voluptas assumenda est, omnis dolor repellendus. Temporibus autem quibusdam et aut officiis debitis aut rerum necessitatibus saepe eveniet ut et voluptates repudiandae sint et molestiae non recusandae. Itaque earum rerum hic tenetur a sapiente delectus.</p>
  <p>Ut aut reiciendis voluptatibus maiores alias consequatur aut perferendis doloribus asperiores repellat cum soluta nobis est eligendi.</p>
</div>

<section class="abs map" role="img" aria-label="Map of the English Midlands with a pin on Birmingham"></section>

<div class="abs office" style="left:131px">
  <h4>VELDA Metals Group</h4>
  <div class="row"><svg width="9" height="12" viewBox="0 0 9 12"><path d="M4.5 0A4.5 4.5 0 0 0 0 4.5C0 8 4.5 12 4.5 12S9 8 9 4.5A4.5 4.5 0 0 0 4.5 0z" fill="#c95316"/><circle cx="4.5" cy="4.5" r="1.6" fill="#fff"/></svg><div>No 15, Maxime placeat possimus,<br>Et harum quidem,<br>London.</div></div>
  <div class="row"><svg width="11" height="11" viewBox="0 0 11 11"><path d="M2 0L4 3 3 4.5C3.8 6 5 7.2 6.5 8L8 7 11 9 9.5 11C4.5 10.5.5 6.5 0 1.5z" fill="#c95316"/></svg><div>Tel: +44 (0) 8888 888 888</div></div>
</div>
<div class="abs office hl" style="left:454px">
  <h4>VELDA Metals Group</h4>
  <div class="row"><svg width="9" height="12" viewBox="0 0 9 12"><path d="M4.5 0A4.5 4.5 0 0 0 0 4.5C0 8 4.5 12 4.5 12S9 8 9 4.5A4.5 4.5 0 0 0 4.5 0z" fill="#fff"/><circle cx="4.5" cy="4.5" r="1.6" fill="#c95316"/></svg><div>No 15, Maxime placeat possimus,<br>Et harum quidem,<br>Birmingham.</div></div>
  <div class="row"><svg width="11" height="11" viewBox="0 0 11 11"><path d="M2 0L4 3 3 4.5C3.8 6 5 7.2 6.5 8L8 7 11 9 9.5 11C4.5 10.5.5 6.5 0 1.5z" fill="#fff"/></svg><div>Tel: +44 (0) 8888 888 888</div></div>
</div>
<div class="abs office" style="left:779px">
  <h4>VELDA Metals Group</h4>
  <div class="row"><svg width="9" height="12" viewBox="0 0 9 12"><path d="M4.5 0A4.5 4.5 0 0 0 0 4.5C0 8 4.5 12 4.5 12S9 8 9 4.5A4.5 4.5 0 0 0 4.5 0z" fill="#c95316"/><circle cx="4.5" cy="4.5" r="1.6" fill="#fff"/></svg><div>No 15, Maxime placeat possimus,<br>Et harum quidem,<br>Jersey</div></div>
  <div class="row"><svg width="11" height="11" viewBox="0 0 11 11"><path d="M2 0L4 3 3 4.5C3.8 6 5 7.2 6.5 8L8 7 11 9 9.5 11C4.5 10.5.5 6.5 0 1.5z" fill="#c95316"/></svg><div>Tel: +44 (0) 8888 888 888</div></div>
</div>

<footer class="abs site-footer"></footer>
<div class="abs footer-brand"><span class="brand-mark"></span><span class="brand-name">VELDA</span><span class="brand-sub" style="font-size:13px">METALS GROUP</span></div>
<div class="abs footer-links">Terms and Conditions &nbsp;|&nbsp; Privacy Policy &nbsp;|&nbsp; Contact Us</div>
<div class="abs social"><span></span><span></span><span></span><span></span><span></span></div>
<div class="abs footer-rule"></div>
<div class="abs copyright">Copyright © 2018 . All Rights Reserved.</div>

</body>
</html>
```